Brain Science Music company needs modern clean website

We're looking for a website that's very clean and modern but also has some nice bold (futuristic) colors in it. The design should communicate a company that's providing something new and fresh! We'd greatly appreciate web designs similar to: https://thevarnishworks.co/

Lumen Cadence is a US-based Neuroscience music company that offers state-of-the-art technology solutions that help people focus, relax and sleep with the help of scientifically engineered music.

Target Market(s)

US businesses looking for specialized neuroscience music technology.

Logo Text

LumenCadence or LC

Coding

Coded - Design and coding required

Number of Pages Required

1 page

Font styles to use
Sans Serif

Colors

Designer to choose colors to be used in the design.

Requirements
Nice to have
• A website similar to: https://thevarnishworks.co/
We like the colors, the fonts, the simple design layouts and the colorful images.

```html
<!DOCTYPE html>
<html lang="en">
<head>
<meta charset="utf-8">
<title>Lumen Cadence</title>
<link rel="stylesheet" href="https://fonts.googleapis.com/css2?family=Poppins:wght@400;500;600;700;800&family=Oswald:wght@500&display=swap">
<style>
:root{
  --ink:#1f1f1f;
  --text:#333333;
  --orange:#f4511e;
  --blue:#1a8fe3;
  --purple:#8a1fe0;
  --navy:#1d3fbf;
  --green:#5cc234;
  --grey:#efefef;
  --card:#f0f0f0;
  --white:#ffffff;
}
*{box-sizing:border-box;margin:0;padding:0}
html,body{width:1200px;height:3369px;overflow:hidden;background:var(--white)}
body{position:relative;font-family:'Poppins',sans-serif;color:var(--text)}
.abs{position:absolute}
.hero-disc{left:530px;top:-230px;width:1020px;height:1020px;border-radius:50%;background:var(--grey)}
.brand{left:73px;top:48px;font-size:36px;font-weight:400;color:var(--ink);letter-spacing:.5px}
.menu{left:1095px;top:62px;width:32px}
.menu span{display:block;height:5px;background:var(--ink);margin-bottom:6px;border-radius:1px}
.hero-title{left:72px;top:240px;font-size:74px;font-weight:800;line-height:.88;color:var(--ink);letter-spacing:1px}
.hero-sub{left:75px;top:396px;font-size:29px;font-weight:600;line-height:42px;color:var(--blue)}
.learn{left:74px;top:520px;font-size:22px;font-weight:600;color:var(--orange)}
.brain-art{left:500px;top:140px;width:630px;height:580px;border-radius:48% 52% 45% 55%/55% 50% 50% 45%;
  background:linear-gradient(100deg,#e6232a 0%,#f58a1f 22%,#f7d21c 40%,#53b848 58%,#2a7fd6 75%,#8b2fb8 100%);opacity:.9}
.section-title{font-size:78px;font-weight:800;color:var(--ink);line-height:1}
.apps-title{left:74px;top:860px}
.apps-sub{left:74px;top:962px;font-size:29px;font-weight:500;color:var(--ink)}
.card{top:1055px;width:240px;height:221px;background:var(--card);border-radius:8px;text-align:center;padding-top:35px}
.card.active{background:var(--white);box-shadow:0 4px 14px rgba(0,0,0,.18)}
.card svg{width:48px;height:48px}
.card h3{font-size:21px;font-weight:700;color:var(--blue);margin-top:10px}
.card p{font-size:14.5px;line-height:24px;margin:6px 22px 0;color:var(--text)}
.wave-title{left:72px;top:1395px;line-height:.95}
.feature-icon{width:76px;height:76px;border-radius:12px;display:flex;align-items:center;justify-content:center}
.feature-text{width:410px;font-size:17.5px;line-height:31.5px;color:var(--text)}
.story-shape{left:0;top:2009px;width:560px;height:625px}
.story-title{left:74px;top:2175px;font-size:78px;font-weight:800;color:var(--white);line-height:.97}
.step-num{width:82px;height:82px;border-radius:50%;background:var(--white);border:3px solid #e9e9e9;
  display:flex;align-items:center;justify-content:center;font-family:'Oswald',sans-serif;font-size:46px;font-weight:500;color:var(--orange)}
.step-text{font-size:17.5px;line-height:31px;color:var(--text)}
.contact{left:0;top:2794px;width:1200px;height:575px;background:var(--grey)}
.contact-title{left:0;top:2855px;width:1200px;text-align:center}
.contact-sub{left:0;top:2950px;width:1200px;text-align:center;font-size:18px;color:var(--ink)}
.email{left:254px;top:2997px;width:692px;height:70px;background:var(--white);text-align:center;line-height:70px;font-size:18px;color:var(--ink)}
.submit{left:436px;top:3082px;width:330px;height:72px;background:var(--orange);color:var(--white);text-align:center;line-height:72px;font-size:30px;font-weight:700}
.footer-nav{left:0;top:3227px;width:1200px;display:flex;justify-content:center;gap:48px;font-size:14.5px;font-weight:600;color:var(--ink)}
.copyright{left:0;top:3258px;width:1200px;text-align:center;font-size:12.5px;color:var(--ink)}
.social{left:0;top:3291px;width:1200px;display:flex;justify-content:center;gap:32px}
.social span{width:24px;height:24px;border-radius:50%;background:#3a3a3a}
</style>
</head>
<body>

<div class="abs hero-disc"></div>
<div class="abs brand">Lumen Cadence</div>
<div class="abs menu"><span></span><span></span><span></span></div>
<div class="abs brain-art" role="img" aria-label="Rainbow paint-splashed brain illustration with flowing sheet music"></div>
<h1 class="abs hero-title">Lumen<br>Cadence</h1>
<p class="abs hero-sub">The new frontier of music<br>and the brain.</p>
<a class="abs learn">Learn More &#8250;</a>

<h2 class="abs section-title apps-title">Applications</h2>
<p class="abs apps-sub">Merging neuroscience and music, creating audio enhancing:</p>

<div class="abs card active" style="left:75px">
  <svg viewBox="0 0 48 48"><g fill="var(--orange)"><rect x="4" y="40" width="40" height="4"/><rect x="4" y="10" width="4" height="32"/><rect x="13" y="28" width="5" height="10"/><rect x="21" y="22" width="5" height="16"/><rect x="29" y="26" width="5" height="12"/><rect x="37" y="16" width="5" height="22"/></g></svg>
  <h3>Productivity</h3>
  <p>Neque porro quisquam est qui dolorem ipsum quia dolor sit amet</p>
</div>
<div class="abs card" style="left:345px">
  <svg viewBox="0 0 48 48"><g fill="var(--orange)"><rect x="2" y="10" width="5" height="30"/><rect x="2" y="30" width="44" height="5"/><rect x="41" y="22" width="5" height="18"/><circle cx="14" cy="20" r="5"/><path d="M21 16h18a6 6 0 0 1 6 6v6H21z"/></g></svg>
  <h3>Sleep</h3>
  <p>Neque porro quisquam est qui dolorem ipsum quia dolor sit amet</p>
</div>
<div class="abs card" style="left:615px">
  <svg viewBox="0 0 48 48"><g fill="var(--orange)"><circle cx="24" cy="8" r="5"/><path d="M24 15c-6 4-8 12-3 20h6c5-8 3-16-3-20z"/><rect x="6" y="38" width="36" height="6" rx="3"/></g></svg>
  <h3>Meditation</h3>
  <p>Neque porro quisquam est qui dolorem ipsum quia dolor sit amet</p>
</div>
<div class="abs card" style="left:885px">
  <svg viewBox="0 0 48 48"><g fill="var(--orange)"><circle cx="32" cy="7" r="5"/><path d="M18 14l14 2-4 12 8 8-4 4-10-10-6 14-6-2 8-22-6 3-3-4z"/></g></svg>
  <h3>Athletics</h3>
  <p>Neque porro quisquam est qui dolorem ipsum quia dolor sit amet</p>
</div>

<h2 class="abs section-title wave-title">Brainwave<br>Entrainment</h2>

<div class="abs feature-icon" style="left:75px;top:1600px;background:var(--orange)">
  <svg width="48" height="40" viewBox="0 0 48 40"><path d="M8 22a8 8 0 0 1 4-14 10 10 0 0 1 18-2 9 9 0 0 1 10 10 7 7 0 0 1-2 13H14a7 7 0 0 1-6-7z" fill="var(--white)"/><path d="M20 31v6M16 18q6-4 10 2M26 12q4 4 10 2" stroke="var(--orange)" stroke-width="2" fill="none"/></svg>
</div>
<p class="abs feature-text" style="left:174px;top:1591px">Neurons in our brains communicate with each other,&nbsp; forming thoughts, emotions, and ideas using electrical&nbsp; impulses (commonly known as Brainwaves).</p>

<div class="abs feature-icon" style="left:615px;top:1600px;background:var(--purple)">
  <svg width="50" height="40" viewBox="0 0 50 40"><g fill="var(--white)"><circle cx="17" cy="20" r="11"/><circle cx="37" cy="11" r="7"/><circle cx="37" cy="30" r="7"/></g><g fill="var(--purple)"><circle cx="17" cy="20" r="4"/><circle cx="37" cy="11" r="2.5"/><circle cx="37" cy="30" r="2.5"/></g></svg>
</div>
<p class="abs feature-text" style="left:705px;top:1591px;width:420px">Lumen Cadence leverages Musical Phase Locking, to optimize brainwave patterns for each desired activity.</p>

<div class="abs feature-icon" style="left:75px;top:1762px;background:var(--navy)">
  <svg width="48" height="44" viewBox="0 0 48 44"><g fill="var(--white)"><circle cx="18" cy="12" r="9"/><path d="M2 40a16 14 0 0 1 28-9v9z"/><circle cx="36" cy="32" r="10"/></g><path d="M36 26v6h5" stroke="var(--navy)" stroke-width="2.5" fill="none"/></svg>
</div>
<p class="abs feature-text" style="left:174px;top:1753px">Activities such as sleeping, working, or meditating, each have their own unique brainwave pattern.</p>

<div class="abs feature-icon" style="left:615px;top:1762px;background:var(--green)">
  <svg width="40" height="40" viewBox="0 0 40 40"><g fill="var(--white)"><path d="M12 8l22-5v24h-5V10l-12 3v19h-5z"/><ellipse cx="10" cy="32" rx="6" ry="5"/><ellipse cx="29" cy="27" rx="6" ry="5"/></g></svg>
</div>
<p class="abs feature-text" style="left:705px;top:1753px;width:420px">Our music is driven by science. We utilize large scale studies and data from electro- encephlograms to produce substantial results.</p>

<svg class="abs story-shape" viewBox="0 0 560 625" aria-hidden="true"><path d="M0 0H534C560 200 520 520 0 625Z" fill="var(--blue)"/></svg>
<h2 class="abs story-title">Elias’s<br>Story</h2>

<div class="abs step-num" style="left:503px;top:2036px">01</div>
<p class="abs step-text" style="left:608px;top:2026px;width:500px">Founder and Team Leader of Lumen Cadence, in conjunction with primary scientific advisor Dr. Nora Halvorsen. Elias is a pioneer in the neuroscience of music, and key innovator on the technology of Musical Phase Locking.</p>

<div class="abs step-num" style="left:498px;top:2205px">02</div>
<p class="abs step-text" style="left:602px;top:2208px;width:540px">At the age of 10, Elias wrote his first symphony and began studying music composition</p>

<div class="abs step-num" style="left:452px;top:2311px">03</div>
<p class="abs step-text" style="left:546px;top:2319px;width:580px">After exposure to alpha waves in music, Elias began a lifelong pursuit of merging neuroscience and music composition</p>

<div class="abs step-num" style="left:392px;top:2405px">04</div>
<p class="abs step-text" style="left:492px;top:2413px;width:620px;line-height:30px">Elias founded Clearfield Labs in 2003, creating audio workstations for those who wanted to experience the effects of music guided by neuroscience, as well as software for brain-computer interfaces..</p>

<div class="abs step-num" style="left:277px;top:2511px">05</div>
<p class="abs step-text" style="left:377px;top:2519px;width:700px;line-height:29px">As the science progressed and Clearfield Labs grew, Elias decided to form Tuneframe.app in 2014, a website and app that allowed nearly anybody to access the music, not just those who were scientifically minded.</p>

<div class="abs step-num" style="left:75px;top:2606px">06</div>
<p class="abs step-text" style="left:174px;top:2616px;width:720px">Lumen Cadence was formed to further the vision of neuroscience-based music becoming a daily resource that everyone should experience.</p>

<div class="abs contact"></div>
<h2 class="abs section-title contact-title">Get in Touch</h2>
<p class="abs contact-sub">Neque porro quisquam est qui dolorem ipsum quia dolor sit amet</p>
<div class="abs email">Enter Your Email</div>
<div class="abs submit">Submit</div>

<nav class="abs footer-nav"><span>HOME</span><span>ABOUT US</span><span>SERVICES</span><span>BLOG</span><span>RESOURCES</span><span>CONTACT US</span></nav>
<p class="abs copyright">Copyright © 2021 CompanyName. All rights reserved</p>
<div class="abs social"><span></span><span></span><span></span><span></span><span></span></div>

</body>
</html>
```